Restaurant menu design

I need a menu for a restaurant in Spain.
It has to be bohemian but modern. We need something romantic and elegant.
The restaurant is elegant with good food and an excellent reputation. It is also modern at the same time.
The restaurant is superbly decorated and very chick so we need something "class" to fit in with the surroundings.
The size of the document must be 325 mm in high and 245 mm as a maximum and preferably made in indesign.

Reason: Thank you all for your designs.
So far all your designs are ok but it isn´t what we are looking for. Most of the designs are too loaded, too many colors and too much decoration.

Target Market(s)

Adults of various age groups and different nationalities mostly European.

Industry/Entity Type

Restaurant

Requirements
Must have
• The menu must have two interior pages with the text as in the document attached.It must be easily legible.
Nice to have
• See what kind of menus they use in important restaurants in places like Paris, see what designs are in trend, but Not necessarily doing the same style if it doesn’t fit in with the description above.
Should not have
• Nothing old fashioned.

```html
<!DOCTYPE html>
<html lang="es">
<head>
<meta charset="utf-8">
<title>La Violette — Carta</title>
<link rel="stylesheet" href="https://fonts.googleapis.com/css2?family=Great+Vibes&family=Crimson+Text:ital,wght@1,400;1,600&display=swap">
<style>
  :root{
    --backdrop:#ececec;
    --cream:#fbf1d9;
    --cream-light:#fdf8ea;
    --wine:#7a1446;
    --wine-dark:#5f0e36;
    --gold:#d2a53c;
    --gold-light:#f3d98a;
    --ink:#2b1a14;
    --price:#8b1a46;
  }
  *{margin:0;padding:0;box-sizing:border-box}
  html,body{width:1200px;height:833px;overflow:hidden;background:var(--backdrop)}
  .spread{position:absolute;left:48px;top:52px;width:1075px;height:714px;overflow:hidden;box-shadow:0 4px 14px rgba(0,0,0,.18)}
  .page{position:absolute;top:0;height:100%;width:537.5px;overflow:hidden;background:radial-gradient(ellipse at 50% 40%,var(--cream-light),var(--cream) 75%)}
  .page--left{left:0}
  .page--right{left:537.5px}
  .page--left::after,.page--right::after{content:"";position:absolute;top:0;bottom:0;width:30px}
  .page--left::after{right:0;background:linear-gradient(90deg,transparent,rgba(120,90,40,.12))}
  .page--right::after{left:0;background:linear-gradient(270deg,transparent,rgba(120,90,40,.12))}
  .band{position:absolute;top:0;height:100%;background:var(--wine)}
  .page--left .band{left:0;width:77px}
  .page--right .band{right:0;width:97px}
  .gold-rule{position:absolute;top:0;height:100%;width:10px;background:linear-gradient(180deg,var(--gold),var(--gold-light) 45%,var(--gold) 70%,var(--gold-light))}
  .page--left .gold-rule{left:77px}
  .page--right .gold-rule{right:78px}

  .section{position:absolute;font-family:"Crimson Text",Georgia,serif;font-style:italic;color:var(--ink)}
  .section h2{font-family:"Great Vibes",cursive;font-weight:400;font-size:30px;color:var(--wine);line-height:30px;height:32px}
  .rule{position:relative;height:1px;background:var(--wine);margin-top:1px}
  .rule::after{content:"";position:absolute;top:-2px;height:4px;width:57px;background:var(--wine-dark)}
  .page--left .rule::after{right:0}
  .page--right .rule::after{left:0}
  .page--right .section h2{text-align:right}

  .items{list-style:none;margin-top:28px}
  .item{display:flex;align-items:baseline;height:13px;font-size:9.6px;line-height:13px;white-space:nowrap}
  .leader{flex:1;border-bottom:1px dotted rgba(43,26,20,.7);margin:0 3px;transform:translateY(-2px);min-width:10px}
  .price{font-weight:600;color:var(--price)}
  .page--left .price{width:38px;text-align:right}
  .page--right .price{width:36px}
  .item--wrap{justify-content:flex-end}

  .entradas{left:143px;top:50px;width:335px}
  .pescados{left:143px;top:327px;width:335px}
  .ninos{left:143px;top:537px;width:335px}
  .carnes{left:58px;top:50px;width:345px}
  .salsas{left:58px;top:336px;width:345px}
  .postres{left:58px;top:476px;width:345px}
  .carnes .items{margin-top:18px}
  .salsas .items,.postres .items{margin-top:18px}
</style>
</head>
<body>
<main class="spread">
  <section class="page page--left">
    <div class="band"></div><div class="gold-rule"></div>

    <div class="section entradas">
      <h2>Entradas</h2><div class="rule"></div>
      <ul class="items">
        <li class="item">Ensalada La Violette. Lechuga, tomate<span class="leader"></span><span class="price">7,75 €</span></li>
        <li class="item">Ensalada Caprese (Tomate y Mozzarella)<span class="leader"></span><span class="price">7,75 €</span></li>
        <li class="item">Escarola al Queso de Cabra con Bacon<span class="leader"></span><span class="price">6,75 €</span></li>
        <li class="item">Cocktail de Gambas, Langostinos y Aguacate<span class="leader"></span><span class="price">7,50 €</span></li>
        <li class="item">La Sopa de Pescado<span class="leader"></span><span class="price">8,25 €</span></li>
        <li class="item">Crema de Espárragos Trigueros y Calabacín<span class="leader"></span><span class="price">5,95 €</span></li>
        <li class="item">Carpaccio de Ternera<span class="leader"></span><span class="price">11,50 €</span></li>
        <li class="item">Carpaccio de Salmón al Eneldo<span class="leader"></span><span class="price">9,75 €</span></li>
        <li class="item">Carpaccio de Atún<span class="leader"></span><span class="price">13,95 €</span></li>
        <li class="item">Melón con Jamón Ibérico<span class="leader"></span><span class="price">9,25 €</span></li>
        <li class="item">Parrillada de Verduras<span class="leader"></span><span class="price">7,95 €</span></li>
        <li class="item">Parrillada de Verduras Gratinada al Queso de Cabra<span class="leader"></span><span class="price">8,95 €</span></li>
        <li class="item">Gambas Roja de la Bahía<span class="leader"></span><span class="price">12,95 €</span></li>
      </ul>
    </div>

    <div class="section pescados">
      <h2>Pescados al Grill</h2><div class="rule"></div>
      <ul class="items">
        <li class="item">Lubina al Hinojo<span class="leader"></span><span class="price">15,50 €</span></li>
        <li class="item">Lubina Fileteada y su Salsa Rústica con Berenjena<span class="leader"></span><span class="price">18,50 €</span></li>
        <li class="item">Filete de Rodaballo y su Salsa de Marisco<span class="leader"></span><span class="price">17,25 €</span></li>
        <li class="item">Dorada del Mediterráneo<span class="leader"></span><span class="price">13,95 €</span></li>
        <li class="item">Lenguado al Grill con Hierbas Provenzales<span class="leader"></span><span class="price">20,75 €</span></li>
        <li class="item">Pieza de Atún Fresco y su Salsa Griega<span class="leader"></span><span class="price">18,95 €</span></li>
        <li class="item">Lomo de Salmón con Salsa de Frambuesa<span class="leader"></span><span class="price">11,25 €</span></li>
        <li class="item">Parrillada de Pescado y Marisco<span class="leader"></span><span class="price">23,50 €</span></li>
      </ul>
    </div>

    <div class="section ninos">
      <h2>Especial Niños</h2><div class="rule"></div>
      <ul class="items">
        <li class="item">Solomillo Junior, huevo y patatas fritas<span class="leader"></span><span class="price">6,25 €</span></li>
        <li class="item">Fish &amp; chips<span class="leader"></span><span class="price">6,25 €</span></li>
      </ul>
    </div>
  </section>

  <section class="page page--right">
    <div class="band"></div><div class="gold-rule"></div>

    <div class="section carnes">
      <h2>Carnes</h2><div class="rule"></div>
      <ul class="items">
        <li class="item"><span class="price">11,95 €</span><span class="leader"></span>Pechuga de Pollo “Marie France” con Champiñones y Bacon.</li>
        <li class="item"><span class="price">14,50 €</span><span class="leader"></span>Chuletas de Cordero.</li>
        <li class="item"><span class="price">9,95 €</span><span class="leader"></span>Costillas de Cerdo con Salsa Barbacoa.</li>
        <li class="item"><span class="price">19,75 €</span><span class="leader"></span>Paletilla de Cordero Lechal.</li>
        <li class="item item--wrap">Le Strogonoff. Finas tiras de Solomillo con su Salsa de</li>
        <li class="item"><span class="price">15,90 €</span><span class="leader"></span>Champiñones.</li>
        <li class="item"><span class="price">18,50 €</span><span class="leader"></span>Solomillo de Ternera.</li>
        <li class="item item--wrap">Solomillo de Ternera a la Ibérica con Jamón Ibérico y ligera</li>
        <li class="item"><span class="price">20,75 €</span><span class="leader"></span>salsa de Vino Tinto.</li>
        <li class="item"><span class="price">14,50 €</span><span class="leader"></span>“Hamburger Maison Steak Haché”. Picata de Solomillo de</li>
        <li class="item item--wrap"><span class="leader"></span>Ternera, Huevo Frito y Patatas Fritas.</li>
        <li class="item"><span class="price">14,25 €</span><span class="leader"></span>Solomillo de Cerdo al Horno con Bacon y su Salsa de Setas.</li>
        <li class="item"><span class="price">14,75 €</span><span class="leader"></span>Entrecôte de Ternera.</li>
        <li class="item"><span class="price">16,75 €</span><span class="leader"></span>T-Bone Steak de Ternera.</li>
        <li class="item"><span class="price">20,25 €</span><span class="leader"></span>Chuletón de Ternera.</li>
        <li class="item"><span class="price">21,50 €</span><span class="leader"></span>Parrillada de Carnes y Embutidos.</li>
      </ul>
    </div>

    <div class="section salsas">
      <h2>Salsas</h2><div class="rule"></div>
      <ul class="items">
        <li class="item"><span class="price">2,85 €</span><span class="leader"></span>Pimienta.</li>
        <li class="item"><span class="price">2,95 €</span><span class="leader"></span>Roquefort.</li>
        <li class="item"><span class="price">2,95 €</span><span class="leader"></span>Bearnaise.</li>
        <li class="item"><span class="price">2,65 €</span><span class="leader"></span>de Champiñones.</li>
      </ul>
    </div>

    <div class="section postres">
      <h2>Los Postres de la Violette</h2><div class="rule"></div>
      <ul class="items">
        <li class="item"><span class="price">6,25 €</span><span class="leader"></span>Frambuesas “La Violette”.</li>
        <li class="item"><span class="price">5,25 €</span><span class="leader"></span>Cocktail de Frutas Exóticas.</li>
        <li class="item"><span class="price">5,50 €</span><span class="leader"></span>Sorbete de Limón, Coulis de Fresa y Vodka.</li>
        <li class="item"><span class="price">6,25 €</span><span class="leader"></span>Pastel de Chocolate Casero con su Salsa de Vainilla.</li>
        <li class="item"><span class="price">6,25 €</span><span class="leader"></span>Crème Brulée.</li>
        <li class="item"><span class="price">6,95 €</span><span class="leader"></span>Tarta de Manzana Casera “Tatín” y su Helado de Vainilla.</li>
        <li class="item"><span class="price">6,75 €</span><span class="leader"></span>Copa Glacier Nord.</li>
        <li class="item"><span class="price">5,95 €</span><span class="leader"></span>Pera al Chocolate Caliente y Helado de Macadamia.</li>
        <li class="item"><span class="price">5,75 €</span><span class="leader"></span>Tarta de Queso con Coulis de Fresa.</li>
        <li class="item"><span class="price">5,75 €</span><span class="leader"></span>Nuestra Mousse de Chocolate.</li>
      </ul>
    </div>
  </section>
</main>
</body>
</html>
```